Business Card

I need a business card that really pops for a potential customer or person who refers a personal injury lead. I want to highlight our office locations, but only address that needs to be on the card is my office's main address. I want a sleek, modern and minimalist design.

```html
<!DOCTYPE html>
<html lang="en">
<head>
<meta charset="utf-8">
<title>Northfield Injury Lawyers — Business Card</title>
<link href="https://fonts.googleapis.com/css2?family=Montserrat:wght@300;400;500;700&display=swap" rel="stylesheet">
<style>
  :root {
    --backdrop: #1c1c1c;
    --card-dark: #333333;
    --card-light: #ffffff;
    --ink-dark: #1f1f1f;
    --ink-light: #f4f4f4;
    --ink-muted: #555555;
  }
  * { margin: 0; padding: 0; box-sizing: border-box; }
  html, body {
    width: 1200px; height: 1108px; overflow: hidden;
    background: var(--backdrop);
    font-family: "Montserrat", sans-serif;
  }
  .canvas {
    position: relative; width: 1200px; height: 1108px;
    display: flex; flex-direction: column; align-items: center; justify-content: center; gap: 80px;
  }
  .card {
    position: relative; width: 700px; height: 400px;
    box-shadow: 0 12px 30px rgba(0,0,0,.45);
  }
  .card--front { background: var(--card-dark); color: var(--ink-light); }
  .card--back { background: var(--card-light); color: var(--ink-dark); }

  /* Neutral firm-name placeholder: one colour, one weight, plain square */
  .firm-name {
    display: flex; align-items: center; gap: 12px;
    font-weight: 500; letter-spacing: 0; line-height: 1.2;
  }
  .firm-name__square { flex: none; background: currentColor; }

  .card--front .firm-name {
    position: absolute; left: 0; right: 0; top: 150px;
    justify-content: center; font-size: 34px;
  }
  .card--front .firm-name__square { width: 22px; height: 22px; }
  .front-url {
    position: absolute; left: 0; right: 0; bottom: 62px; text-align: center;
    font-size: 15px; font-weight: 300; letter-spacing: .04em;
  }

  .card--back .firm-name { position: absolute; left: 48px; top: 76px; font-size: 24px; }
  .card--back .firm-name__square { width: 16px; height: 16px; }

  .person { position: absolute; right: 40px; top: 52px; text-align: right; }
  .person__name { font-size: 22px; font-weight: 700; }
  .person__title {
    display: inline-block; font-size: 13px; font-weight: 400; margin-top: 3px;
    padding: 0 0 3px 28px; border-bottom: 1.5px solid var(--ink-dark);
  }

  .social { position: absolute; right: 40px; top: 148px; list-style: none; text-align: right; }
  .social li { font-size: 14px; margin-bottom: 10px; display: flex; justify-content: flex-end; align-items: center; gap: 10px; }
  .social__mark { width: 13px; height: 13px; background: var(--ink-dark); border-radius: 2px; }

  .address { position: absolute; left: 48px; top: 232px; font-size: 15px; line-height: 1.25; font-style: normal; }

  .contact { position: absolute; left: 48px; top: 296px; list-style: none; }
  .contact li { display: flex; align-items: center; gap: 14px; font-size: 16px; line-height: 1.3; }
  .contact svg { width: 14px; height: 14px; fill: var(--ink-muted); flex: none; }
</style>
</head>
<body>
<main class="canvas">
  <section class="card card--front" aria-label="Card front">
    <p class="firm-name"><span class="firm-name__square"></span>Northfield Injury Lawyers</p>
    <p class="front-url">www.northfieldlaw.com</p>
  </section>

  <section class="card card--back" aria-label="Card back">
    <p class="firm-name"><span class="firm-name__square"></span>Northfield Injury Lawyers</p>

    <div class="person">
      <p class="person__name">Dale Hartman</p>
      <p class="person__title">CEO &amp; Founder</p>
    </div>

    <ul class="social">
      <li>@northfieldlaw <span class="social__mark"></span></li>
      <li>/northfieldlaw <span class="social__mark"></span></li>
    </ul>

    <address class="address">418 Cedar Grove Ave, #310<br>Lakewood, OH 44107</address>

    <ul class="contact">
      <li>
        <svg viewBox="0 0 16 16" aria-hidden="true"><path d="M3 1h3l1.5 4-2 1.3a9 9 0 0 0 4.2 4.2L11 8.5l4 1.5v3a2 2 0 0 1-2 2A12 12 0 0 1 1 3a2 2 0 0 1 2-2z"/></svg>
        555 310-4821
      </li>
      <li>
        <svg viewBox="0 0 16 16" aria-hidden="true"><path d="M1 3h14v10H1z M1 3l7 6 7-6" stroke="#fff" stroke-width="1.2"/></svg>
        info@northfieldlaw.com
      </li>
      <li>
        <svg viewBox="0 0 16 16" aria-hidden="true"><circle cx="8" cy="8" r="7"/><path d="M1 8h14M8 1c-3 3.5-3 10.5 0 14M8 1c3 3.5 3 10.5 0 14" stroke="#fff" stroke-width="1" fill="none"/></svg>
        www.northfieldlaw.com
      </li>
    </ul>
  </section>
</main>
</body>
</html>
```